Business card design needed

Need a business card for a new Company in Melbourne called Brightway Lending Choices. This company is a Mortgage Brokering company that facilitates mainly Residential loans, but also Business and Commercial loans.
I would like something professional as I am in the finance industry.
I would like Brightway Lending font wise to be bigger than choices, with the word choices to sit below the Brightway Lending.

Industry/Entity Type

Finance

Contact Information for Business Card

Daniel Westhorpe | Lending Specialist
Brightway Lending Choices
P.O Box 517 Elmvale Vic.3071
T. +61 3 9000 4171 | F. +61 3 9000 6235| M. +61 400572904
www.brightwaylending.example

Daniel Westhorpe is a credit representative (CRN 572914)of KRVMO Pty.Ltd (Australian Credit Licence No 648502)

Requirements
Must have
• Daniel Westhorpe is a credit representative (CRN 572914)of KRVMO Pty.Ltd (Australian Credit Licence No 648502) has to sit at the bottom of the card, in the smallest readable font.

The logo to be designed is the most crucial thing for me.

```html
<!DOCTYPE html>
<html lang="en">
<head>
<meta charset="utf-8">
<title>Brightway Lending Choices – Business Card</title>
<link rel="stylesheet" href="https://fonts.googleapis.com/css2?family=Oswald:wght@500&family=Roboto+Condensed:wght@400;700&display=swap">
<style>
  :root {
    --navy: #0057a8;
    --sky: #00aeef;
    --white: #ffffff;
    --ink: #1d1d1d;
    --muted: #e9f6fd;
    --bg-top: #ffffff;
    --bg-bottom: #dcdcdc;
  }
  * { margin: 0; padding: 0; box-sizing: border-box; }
  html, body { width: 1200px; height: 1000px; overflow: hidden; }
  body {
    position: relative;
    background: radial-gradient(ellipse at 50% 35%, var(--bg-top) 0%, #f1f1f1 55%, var(--bg-bottom) 100%);
    font-family: "Roboto Condensed", Arial, sans-serif;
    color: var(--ink);
  }

  /* Brand wordmark: name on one line, "Choices" right-aligned below */
  .wordmark {
    font-family: "Oswald", "Arial Narrow", sans-serif;
    font-weight: 500;
    color: var(--navy);
    text-transform: uppercase;
    line-height: 1;
    white-space: nowrap;
  }
  .wordmark .name { display: block; }
  .wordmark .sub { display: block; text-align: right; }

  .hero-mark {
    position: absolute;
    left: 215px;
    top: 100px;
    width: 735px;
  }
  .hero-mark .name { font-size: 84px; }
  .hero-mark .sub { font-size: 52px; margin-top: 12px; }

  /* Cards */
  .card {
    position: absolute;
    width: 600px;
    height: 340px;
    box-shadow: 0 8px 18px rgba(0,0,0,0.25);
  }

  .card-front {
    left: 40px;
    top: 430px;
    background: var(--navy);
  }
  .card-front .wordmark {
    position: absolute;
    left: 110px;
    top: 105px;
    width: 370px;
    color: var(--white);
  }
  .card-front .name { font-size: 42px; }
  .card-front .sub { font-size: 24px; margin-top: 4px; }
  .card-front .web {
    position: absolute;
    left: 110px;
    width: 370px;
    top: 222px;
    text-align: center;
    font-weight: 700;
    font-size: 17px;
    color: var(--sky);
    white-space: nowrap;
  }

  .card-back {
    left: 560px;
    top: 590px;
    background: var(--white);
  }
  .card-back .wordmark {
    position: absolute;
    left: 20px;
    top: 42px;
    width: 245px;
  }
  .card-back .name { font-size: 28px; }
  .card-back .sub { font-size: 17px; margin-top: 3px; }

  .holder {
    position: absolute;
    left: 300px;
    top: 40px;
    white-space: nowrap;
  }
  .holder-name { font-size: 25px; color: var(--navy); }
  .holder-role { font-size: 15px; font-style: italic; margin-top: 2px; }

  .contacts {
    position: absolute;
    left: 300px;
    top: 118px;
    list-style: none;
    font-size: 16px;
    line-height: 22px;
    white-space: nowrap;
  }
  .contacts li { display: flex; }
  .contacts .label { width: 28px; font-weight: 700; color: var(--navy); }

  .card-band {
    position: absolute;
    left: 0; right: 0; bottom: 0;
    height: 92px;
    background: var(--sky);
    color: var(--white);
    text-align: center;
    padding-top: 12px;
    white-space: nowrap;
  }
  .band-address { font-size: 16px; }
  .band-web { font-size: 17px; font-weight: 700; margin-top: 2px; }
  .band-legal { font-size: 10px; margin-top: 10px; color: var(--muted); }
</style>
</head>
<body>

  <header class="wordmark hero-mark">
    <span class="name">Brightway Lending</span>
    <span class="sub">Choices</span>
  </header>

  <section class="card card-front">
    <div class="wordmark">
      <span class="name">Brightway Lending</span>
      <span class="sub">Choices</span>
    </div>
    <p class="web">www.brightwaylending.example</p>
  </section>

  <section class="card card-back">
    <div class="wordmark">
      <span class="name">Brightway Lending</span>
      <span class="sub">Choices</span>
    </div>

    <div class="holder">
      <p class="holder-name">Daniel Westhorpe</p>
      <p class="holder-role">Lending Specialist</p>
    </div>

    <ul class="contacts">
      <li><span class="label">T</span><span>+ 61 3 9000 4171</span></li>
      <li><span class="label">F</span><span>+ 61 3 9000 6235</span></li>
      <li><span class="label">M</span><span>+ 61 400 572 904</span></li>
    </ul>

    <footer class="card-band">
      <p class="band-address">Lending Specialist Brightway Lending Choices P.O Box 517 Elmvale Vic.3071</p>
      <p class="band-web">www.brightwaylending.example</p>
      <p class="band-legal">Daniel Westhorpe is a credit representative (CRN 572914) of KRVMO Pty. Ltd (Australian Credit Licence No 648502)</p>
    </footer>
  </section>

</body>
</html>
```